【本のタイトル】
●パート主婦が口ぐせを変えて手作り雑貨の通販サイトを始めて
2年で月商200万円に育てた道のり

※本編を参考資料としてつけます

●読者プレゼントは
文面の中にもありますが、森田恭平先生主催のサンセットベルというトーク公演の時に登壇して私が話した内容の動画を、改めて撮影してユーチューブの限定公開にしたものをプレゼントします。

【デザイナーさんにお願いです】

これは、「絶対こうしてください」ということではないのですが、
「できたら、したい」というお願いです。

本編をお読みいただくとわかりますように、
私の人生が森田恭平先生の著書との出会いによって、
大きく変わり、この本の中にも、森田先生のエッセンスが、
たくさん詰まっています。
また、先生への感謝のサプライズとしての意味合いの出版でもあります。♬(^^♪

ですから、表紙デザインのモチーフとして、

例えばですが、
森田恭平先生の
・教材「ロケットチャレンジワーク」のダイナマイトイラストのモチーフが入っている
・ご著書「迷いの霧の晴らし方」のピンク色に黒ゴシックのタイトル、
プレゼントが黄色の丸、という組み合わせ
※ココでいう迷いの霧の晴らし方は、2006年に発売開始した時はピンク色の表紙でした。昨年同じ内容で表紙が飛び込みするような人の表紙カバーになりましたけど、私のイメージは最初のショッキングピンクの表紙のものです
・「弱気な朝に読む帳」「遠い友へ届ける手紙」のイメージ

など、「あからさまじゃないけど、エッセンス入ってる」
みたいなデザインにしたいと考えています。

本文のモチーフがかわいいイラストで描かれていて惹かれました。

ご提案くださいまして、本当にありがとうございます。皆様の素敵なご提案がたくさんあって迷いました。また次回もよろしくお願いいたします。

```html
<!DOCTYPE html>
<html lang="ja">
<head>
<meta charset="utf-8">
<title>パート主婦が口ぐせを変えて手作り雑貨の通販サイトを始めて2年で月商200万円に育てた道のり</title>
<link rel="stylesheet" href="https://fonts.googleapis.com/css2?family=Noto+Sans+JP:wght@700;900&display=swap">
<style>
  :root{
    --pink:#e8287d;
    --pink-deep:#d81c6e;
    --yellow:#ffe833;
    --ink:#111111;
    --white:#ffffff;
  }
  html,body{margin:0;padding:0;overflow:hidden;background:#fff;}
  .cover{
    position:relative;width:750px;height:1200px;overflow:hidden;
    font-family:"Noto Sans JP",sans-serif;color:var(--ink);
  }
  .cover p,.cover h1{margin:0;}
  .cover-photo{
    position:absolute;left:0;top:0;width:750px;height:800px;
    background:
      linear-gradient(180deg,rgba(255,255,255,0) 55%,rgba(190,190,185,.6) 100%),
      linear-gradient(100deg,#5f8a4a 0%,#86a86a 30%,#b8c3b3 55%,#8b8f96 75%,#c9ccd0 100%);
  }
  .outlined{
    -webkit-text-stroke:10px var(--white);
    paint-order:stroke fill;
  }
  .author{
    position:absolute;top:22px;left:0;width:750px;text-align:center;
    color:var(--pink);font-weight:900;white-space:nowrap;
  }
  .author-label{font-size:32px;margin-right:16px;}
  .author-name{font-size:44px;letter-spacing:2px;}
  .title{
    position:absolute;top:296px;left:0;width:750px;text-align:center;
    font-weight:900;font-size:50px;line-height:60px;white-space:nowrap;
  }
  .title-line{display:block;}
  .headline{
    position:absolute;top:596px;left:0;width:750px;text-align:center;
    font-weight:900;color:var(--pink);font-size:104px;line-height:130px;white-space:nowrap;
    -webkit-text-stroke:14px var(--white);paint-order:stroke fill;
  }
  .headline-digit{font-size:150px;color:var(--pink-deep);}
  .title-tail{
    position:absolute;top:718px;left:0;width:750px;text-align:center;
    font-weight:900;font-size:48px;white-space:nowrap;
  }
  .message-band{
    position:absolute;left:0;top:795px;width:750px;height:405px;background:var(--pink);
  }
  .message-heading{
    position:absolute;top:4px;left:0;width:750px;display:flex;align-items:center;justify-content:center;gap:18px;
    color:var(--white);font-weight:700;font-size:27px;
  }
  .message-heading::before,.message-heading::after{
    content:"";width:110px;height:3px;background:var(--white);
  }
  .message-lines{
    position:absolute;top:32px;left:26px;margin:0;padding:0;list-style:none;
    color:var(--white);font-weight:700;font-size:29px;line-height:52px;white-space:nowrap;
  }
  .reader-gift{
    position:absolute;left:592px;top:140px;width:152px;height:200px;
    background:var(--yellow);border-radius:38px;
    display:flex;flex-direction:column;justify-content:center;align-items:center;text-align:center;
    font-weight:700;font-size:13.5px;line-height:20px;color:var(--ink);
  }
  .reader-gift .gift-word{font-size:20px;font-weight:900;color:var(--pink);margin-top:4px;}
  .reader-limited{
    position:absolute;left:598px;top:352px;width:140px;height:44px;
    background:var(--pink-deep);border:3px solid var(--yellow);border-radius:8px;box-sizing:border-box;
    color:var(--white);font-weight:900;font-size:24px;line-height:38px;text-align:center;
  }
</style>
</head>
<body>
<main class="cover">
  <div class="cover-photo" role="img" aria-label="母親と幼い娘が手をつないで明るい並木道を歩く後ろ姿の写真"></div>

  <p class="author">
    <span class="author-label outlined">著者</span><span class="author-name outlined">松下晴美</span>
  </p>

  <h1 class="title">
    <span class="title-line outlined">パート主婦が口ぐせを変えて</span>
    <span class="title-line outlined">手作り雑貨の通販サイトを</span>
    <span class="title-line outlined">始めて</span>
    <span class="title-line outlined">2年で</span>
  </h1>
  <p class="headline">月商<span class="headline-digit">2</span>00万円</p>
  <p class="title-tail outlined">に育てた道のり</p>

  <section class="message-band">
    <p class="message-heading">今できることは、何か・・</p>
    <ul class="message-lines">
      <li>この質問を自分に投げかける時が、チャンスです。</li>
      <li>あなたの潜在意識が、試されるときです。</li>
      <li>あなたは、なんと答えるのでしょう・・</li>
      <li>成功は、そこにあります。</li>
      <li>あなたの心に、この本を、</li>
      <li>読み聴かせてあげてください。</li>
      <li>答えは、そこにあります!!</li>
    </ul>
    <div class="reader-gift">
      <span>森田恭平先生主催の</span>
      <span>サンセットベルで</span>
      <span>登壇したトーク</span>
      <span>内容の動画</span>
      <span>「まどべの灯りで</span>
      <span>明日を描く」</span>
      <span class="gift-word">プレゼント</span>
    </div>
    <div class="reader-limited">読者限定</div>
  </section>
</main>
</body>
</html>
```